Topics to Raise With a Clinician tri-fold brochure

We are looking for a 1 page (front and back) 8.5" x 11" tri-fold brochure. Please refer back to our Rack Cards for a similar look and feel to the design. They can be found here: https://otvenrix.org/resources/sunny-garden-steady-mind-rack-card-series/.
This brochure is titled: Topics to Raise With a Clinician on Forgetfulness.

The document is for older readers. Do not put text over graphics and keep it simple and easy to read with high contrast.

We want some very simple design element(s) incorporated that convey Native American communities or heritage. But NO headdress, teepee graphics, owls etc. I have included some images, please use your creative discretion to use which ones look good.

Please remember to include the funding statement - it can be in a very small font 6/7 point: For more information about our project, please visit https://otvenrix.org/mind-care/resources - This rack card is supported by the Bureau for Wellness Tracking and Outreach (BWTO) of the Federal Office of Wellbeing and Family Supports (FWF) as part of a financial assistance award totaling $1,048,206.52 with 100 percent funded by BWTO/FWF. The contents are those of the author(s) and do not necessarily represent the official views of, nor an endorsement, by BWTO/FWF, or the the national government.

Please feel free to choose one of each of the 2 logos that looks best (horizontal or square). We have the OT3 logo and the Cedar Path Learning Hub logo we would like to add. I have added the document and there are images to choose from to use.

I am thinking that the front of the tri-fold should have one of the pictures of a patient and doctor talking. I have included several options. Please use your creative discretion to choose what looks best.

Please let me know if you have any questions, thank you!

```html
<!DOCTYPE html>
<html lang="en">
<head>
<meta charset="utf-8">
<title>Topics to Raise With a Clinician on Forgetfulness</title>
<link rel="stylesheet" href="https://fonts.googleapis.com/css2?family=Cabin:wght@700&family=Didact+Gothic&family=Montserrat:wght@700&family=PT+Sans+Narrow:wght@400;700&display=swap">
<style>
:root{
  --ink:#1c1c1c;
  --deep-teal:#223e45;
  --teal:#3b6e73;
  --brown:#5e3934;
  --rose:#a85c52;
  --sand:#ecc9a2;
  --white:#ffffff;
}
*{margin:0;padding:0;box-sizing:border-box}
html,body{width:1200px;height:927px;overflow:hidden;background:var(--white)}
.sheet{position:relative;width:1200px;height:927px;overflow:hidden}
.panel{position:absolute;top:0;height:927px}
.panel--tracker{left:0;width:397px;background:var(--white)}
.panel--resources{left:397px;width:400px;background:var(--deep-teal)}
.panel--cover{left:797px;width:403px;background:var(--white)}
.band{position:absolute;display:block}

/* tracker panel */
.tracker-title{position:absolute;left:15px;top:97px;font:400 20px/1.2 "Didact Gothic",sans-serif;color:var(--ink)}
.tracker-text{position:absolute;left:15px;width:376px;font:17.4px/22px "Didact Gothic",sans-serif;color:var(--ink)}
.tracker-intro{top:144px}
.tracker-link-note{top:276px;width:330px}
.tracker-rule{position:absolute;left:15px;top:350px;width:362px;border-top:1.5px dashed var(--ink)}
.tracker-table{position:absolute;left:18px;top:378px;width:359px;border-collapse:collapse;border:1px solid var(--ink);table-layout:fixed}
.tracker-table th,.tracker-table td{border:1px solid var(--ink)}
.tracker-table th{height:30px;font:700 11px "Montserrat",sans-serif;color:var(--ink);text-align:center}
.tracker-table td{height:24.2px}

/* resources panel */
.res-heading{position:absolute;left:0;width:400px;top:46px;text-align:center;font:700 34px/43px "Cabin",sans-serif;color:var(--white)}
.res-label{position:absolute;left:0;width:400px;text-align:center;font:700 24px/28px "PT Sans Narrow",sans-serif;color:var(--sand)}
.res-link{position:absolute;left:0;width:400px;text-align:center;font:400 23px/28px "PT Sans Narrow",sans-serif;color:var(--white)}
.res-footer{position:absolute;left:15px;width:370px;text-align:center;font:400 10px/12.7px "PT Sans Narrow",sans-serif;color:var(--white)}

/* cover panel */
.brand-name{position:absolute;left:38px;top:50px;width:340px;font:700 21px/25px "PT Sans Narrow",sans-serif;color:var(--deep-teal);text-transform:uppercase}
.cover-title{position:absolute;left:0;width:403px;top:168px;text-align:center;font:700 38px/51px "Cabin",sans-serif;color:var(--deep-teal)}
.cover-image{position:absolute;left:0;top:363px;width:403px;height:564px;background:linear-gradient(180deg,#ffffff 0%,#d9d9d9 30%,#e8e8ea 60%,#c9ccd4 100%)}
</style>
</head>
<body>
<main class="sheet">

  <section class="panel panel--tracker">
    <svg class="band" style="left:0;top:0" width="397" height="31" aria-hidden="true">
      <rect x="0" y="0" width="73" height="31" fill="var(--deep-teal)"/>
      <rect x="73" y="0" width="62" height="31" fill="var(--teal)"/>
      <rect x="135" y="0" width="262" height="31" fill="var(--brown)"/>
    </svg>

    <h2 class="tracker-title">Symptom Tracking:</h2>
    <p class="tracker-text tracker-intro">By tracking symptoms like forgetfulness, confusion, or difficulty with everyday tasks, individuals and their caregivers can provide accurate information to healthcare providers, leading to better planning and support.</p>
    <p class="tracker-text tracker-link-note">A symptom tracker template and examples can be found at :</p>
    <div class="tracker-rule"></div>

    <table class="tracker-table">
      <colgroup><col style="width:64px"><col style="width:68px"><col style="width:82px"><col></colgroup>
      <thead><tr><th>Date</th><th>Time</th><th>Location</th><th>Symptoms &amp; Behavior</th></tr></thead>
      <tbody>
        <tr><td></td><td></td><td></td><td></td></tr><tr><td></td><td></td><td></td><td></td></tr>
        <tr><td></td><td></td><td></td><td></td></tr><tr><td></td><td></td><td></td><td></td></tr>
        <tr><td></td><td></td><td></td><td></td></tr><tr><td></td><td></td><td></td><td></td></tr>
        <tr><td></td><td></td><td></td><td></td></tr><tr><td></td><td></td><td></td><td></td></tr>
        <tr><td></td><td></td><td></td><td></td></tr><tr><td></td><td></td><td></td><td></td></tr>
        <tr><td></td><td></td><td></td><td></td></tr><tr><td></td><td></td><td></td><td></td></tr>
        <tr><td></td><td></td><td></td><td></td></tr><tr><td></td><td></td><td></td><td></td></tr>
        <tr><td></td><td></td><td></td><td></td></tr><tr><td></td><td></td><td></td><td></td></tr>
        <tr><td></td><td></td><td></td><td></td></tr><tr><td></td><td></td><td></td><td></td></tr>
        <tr><td></td><td></td><td></td><td></td></tr>
      </tbody>
    </table>

    <svg class="band" style="left:0;top:902px" width="397" height="25" aria-hidden="true">
      <rect x="0" y="0" width="251" height="25" fill="var(--brown)"/>
      <rect x="251" y="0" width="61" height="25" fill="var(--teal)"/>
      <rect x="312" y="0" width="85" height="25" fill="var(--deep-teal)"/>
    </svg>
  </section>

  <section class="panel panel--resources">
    <svg class="band" style="left:0;top:0" width="400" height="16" aria-hidden="true">
      <rect x="2" y="0" width="138" height="16" fill="var(--teal)"/>
      <rect x="140" y="0" width="201" height="16" fill="var(--rose)"/>
    </svg>

    <h2 class="res-heading">For More Information<br>About Memory Loss</h2>

    <p class="res-label" style="top:174px">Seven Signs of Thinking or Memory<br>Shifts that May Point to Dementia:</p>
    <p class="res-link" style="top:260px">https://go.otvenrix.org/SevenSigns</p>
    <p class="res-label" style="top:318px">Memory Companions Room:</p>
    <p class="res-link" style="top:376px">otvenrix.org/memory-companions/rooms</p>
    <p class="res-label" style="top:434px">Northvale Memory Loss Guide:</p>
    <p class="res-link" style="top:492px">https://go.otvenrix.org/NorthvaleGuide</p>
    <p class="res-label" style="top:549px">Elderwise Questions to Ask:</p>
    <p class="res-link" style="top:607px">https://go.otvenrix.org/ElderwiseQA</p>
    <p class="res-label" style="top:666px">Steady Steps for Living with Dementia:</p>
    <p class="res-link" style="top:723px">https://go.otvenrix.org/SteadySteps</p>

    <p class="res-footer" style="top:791px">For more information about our project, please visit</p>
    <p class="res-footer" style="top:816px">https://otvenrix.org/mind-care/resources</p>
    <p class="res-footer" style="top:842px">This rack card is supported by the Bureau for Wellness Tracking and Outreach (BWTO) of the Federal Office of Wellbeing and Family Supports (FWF) as part of a financial assistance award totaling $1,048,206.52 with 100 percent funded by BWTO/FWF. The contents are those of the author(s) and do not necessarily represent the official views of, nor an endorsement, by BWTO/FWF, or the national government.</p>
  </section>

  <section class="panel panel--cover">
    <svg class="band" style="left:0;top:0" width="403" height="17" aria-hidden="true">
      <rect x="0" y="0" width="296" height="17" fill="var(--deep-teal)"/>
      <rect x="296" y="0" width="107" height="17" fill="var(--rose)"/>
    </svg>

    <p class="brand-name">Council for Elder<br>Kinship Wellness</p>

    <h1 class="cover-title">Topics to Raise<br>With a Clinician<br>on Forgetfulness</h1>

    <div class="cover-image" role="img" aria-label="Photo: three tree-shaped head silhouettes losing leaves above an older man looking up among floating question marks"></div>
  </section>

</main>
</body>
</html>
```